Flyer für einen Sanitär Heizungs Betrieb
Zielgruppe
Sanitär Heizungs Betrieb der den Fokus verstärkt auf den Service an Heizungsanlagen setzten will.
Der Flyer soll sowohl an Privathaushalte als auch an Hausverwaltungen gehen.
Er soll unsere Leistungen aufzeigen und einen guten ersten Eindruck vermitteln.
Aufgabenstellung
Anbei sende ich Themen die als Leistung aufgeführt werden, sowie Strichwort für einen Werbetext (kann gerne generiert werden ansonsten kommt er noch zum texter)

```html
<!DOCTYPE html>
<html lang="de">
<head>
<meta charset="utf-8">
<title>Brenntal GmbH – Flyer</title>
<link rel="stylesheet" href="https://fonts.googleapis.com/css2?family=Source+Sans+3:wght@400;600;700&display=swap">
<style>
  :root {
    --stage: #a3a3a3;
    --paper: #ffffff;
    --blue: #1279c1;
    --red: #e52527;
    --yellow: #fdd000;
    --text: #5a5a5a;
    --font: "Source Sans 3", "Source Sans Pro", Arial, sans-serif;
  }
  * { box-sizing: border-box; margin: 0; padding: 0; }
  html, body { width: 1200px; height: 1134px; overflow: hidden; }
  body { background: var(--stage); font-family: var(--font); position: relative; }

  .flyer { position: absolute; top: 69px; width: 506px; height: 994px; background: var(--paper); padding: 9px; }
  .flyer--services { left: 57px; }
  .flyer--intro { left: 600px; }
  .flyer__inner { position: relative; width: 488px; height: 975px; overflow: hidden; background: var(--paper); }

  .hero { position: absolute; left: 0; top: 0; width: 488px; height: 424px; display: block; }

  .brand { position: absolute; right: 31px; top: 22px; font-size: 23px; font-weight: 700; color: var(--blue); letter-spacing: 0.3px; }

  .headline { position: absolute; font-size: 31px; font-weight: 700; color: var(--blue); line-height: 1; }
  .flyer--services .headline { left: 74px; top: 412px; }
  .flyer--intro .headline { left: 51px; top: 406px; }

  .services { position: absolute; left: 40px; top: 459px; width: 410px; list-style: none; color: var(--text); font-size: 14.5px; line-height: 14.8px; }
  .services > li { position: relative; padding-left: 34px; margin-bottom: 15px; }
  .services .check-circle { position: absolute; left: 0; top: -1px; width: 20px; height: 20px; }
  .services .sub { list-style: none; }
  .services .sub li { position: relative; padding-left: 23px; }
  .services .sub li::before { content: ""; position: absolute; left: 1px; top: 3px; width: 8px; height: 8px; border-radius: 50%; background: var(--red); }

  .facts { position: absolute; left: 31px; top: 452px; width: 440px; list-style: none; color: var(--text); font-size: 14.5px; line-height: 21px; }
  .facts li { position: relative; padding-left: 22px; }
  .facts li.lead { margin-bottom: 18px; }
  .facts .tick { position: absolute; left: 0; top: 1px; width: 14px; height: 14px; }

  .gallery { position: absolute; left: 0; top: 668px; width: 488px; height: 159px; display: flex; gap: 10px; }
  .gallery__tile { flex: 1; height: 100%; }
  .tile--bath { background: linear-gradient(160deg, #3a3a3c 0%, #6d6a66 55%, #c9c3ba 100%); }
  .tile--tech { background: linear-gradient(135deg, #c8ccd0 0%, #f1f1f1 45%, #5b7fa8 100%); }
  .tile--valves { background: linear-gradient(140deg, #d9dde2 0%, #3d6f98 50%, #1f3f5c 100%); }

  .contact { position: absolute; left: 0; top: 829px; width: 488px; height: 107px; background: var(--blue); color: #fff; font-size: 10.8px; line-height: 14px; }
  .contact__col { position: absolute; }
  .contact__col--left { left: 23px; top: 9px; }
  .contact__col--right { left: 289px; top: 5px; }
  .contact__divider { position: absolute; left: 231px; top: 17px; width: 1.5px; height: 79px; background: #fff; }
  .contact__lines { margin-bottom: 5px; }
  .contact__item { position: relative; padding-left: 23px; }
  .contact__item svg { position: absolute; left: 0; top: 1px; width: 13px; height: 12px; }

  .web { position: absolute; left: 0; top: 936px; width: 488px; height: 39px; background: var(--red); color: #fff; font-size: 13.6px; line-height: 39px; text-align: center; padding-right: 12px; }
</style>
</head>
<body>

<section class="flyer flyer--services">
  <div class="flyer__inner">
    <svg class="hero" viewBox="0 0 488 424">
      <defs>
        <linearGradient id="heroPump" x1="0" y1="0" x2="1" y2="1">
          <stop offset="0" stop-color="#e9ede6"/>
          <stop offset="0.35" stop-color="#b9bdb4"/>
          <stop offset="0.6" stop-color="#9a9896"/>
          <stop offset="1" stop-color="#6f6d6b"/>
        </linearGradient>
      </defs>
      <polygon points="0,0 488,0 488,330 0,290" fill="url(#heroPump)" role="img" aria-label="Foto: Luft-Wasser-Wärmepumpe vor einer Holzfassade auf einer Terrasse"/>
      <polygon points="0,290 488,330 488,352 0,312" fill="var(--blue)"/>
      <polygon points="0,318 488,358 488,364 0,324" fill="var(--yellow)"/>
      <polygon points="0,330 488,370 488,374 0,334" fill="var(--red)"/>
    </svg>
    <div class="brand">Brenntal GmbH</div>

    <h1 class="headline">Unsere Leistungen</h1>

    <ul class="services">
      <li>
        <svg class="check-circle" viewBox="0 0 20 20"><path d="M17.2 6.2A8.3 8.3 0 1 0 18.3 10" fill="none" stroke="var(--blue)" stroke-width="1.8" stroke-linecap="round"/><path d="M6 9.5l3.4 3.4L18.5 3.5" fill="none" stroke="var(--blue)" stroke-width="1.8" stroke-linecap="round" stroke-linejoin="round"/></svg>
        Wartung an:
        <ul class="sub">
          <li>Zentralheizung Öl &amp; Gas (alle Hersteller)</li>
          <li>Solaranlagen</li>
          <li>Luft/Wasser Wärmepumpen</li>
          <li>jegliche Gasgeräte (Durchlauferhitzer, Einzelofen Kachelofen. Heizwertthermen etc…)</li>
        </ul>
      </li>
      <li>
        <svg class="check-circle" viewBox="0 0 20 20"><path d="M17.2 6.2A8.3 8.3 0 1 0 18.3 10" fill="none" stroke="var(--blue)" stroke-width="1.8" stroke-linecap="round"/><path d="M6 9.5l3.4 3.4L18.5 3.5" fill="none" stroke="var(--blue)" stroke-width="1.8" stroke-linecap="round" stroke-linejoin="round"/></svg>
        Störungsbeseitigung und Reparaturen an Heizung- und Sanitäranlagen
      </li>
      <li>
        <svg class="check-circle" viewBox="0 0 20 20"><path d="M17.2 6.2A8.3 8.3 0 1 0 18.3 10" fill="none" stroke="var(--blue)" stroke-width="1.8" stroke-linecap="round"/><path d="M6 9.5l3.4 3.4L18.5 3.5" fill="none" stroke="var(--blue)" stroke-width="1.8" stroke-linecap="round" stroke-linejoin="round"/></svg>
        Testen und aufbereiten Ihres Heizungswasser nach VDI 123 Standard
      </li>
      <li>
        <svg class="check-circle" viewBox="0 0 20 20"><path d="M17.2 6.2A8.3 8.3 0 1 0 18.3 10" fill="none" stroke="var(--blue)" stroke-width="1.8" stroke-linecap="round"/><path d="M6 9.5l3.4 3.4L18.5 3.5" fill="none" stroke="var(--blue)" stroke-width="1.8" stroke-linecap="round" stroke-linejoin="round"/></svg>
        Spülen der Heizungsanlagen (Fußbodenheizung)
      </li>
      <li>
        <svg class="check-circle" viewBox="0 0 20 20"><path d="M17.2 6.2A8.3 8.3 0 1 0 18.3 10" fill="none" stroke="var(--blue)" stroke-width="1.8" stroke-linecap="round"/><path d="M6 9.5l3.4 3.4L18.5 3.5" fill="none" stroke="var(--blue)" stroke-width="1.8" stroke-linecap="round" stroke-linejoin="round"/></svg>
        Notdienst Heizung
      </li>
      <li>
        <svg class="check-circle" viewBox="0 0 20 20"><path d="M17.2 6.2A8.3 8.3 0 1 0 18.3 10" fill="none" stroke="var(--blue)" stroke-width="1.8" stroke-linecap="round"/><path d="M6 9.5l3.4 3.4L18.5 3.5" fill="none" stroke="var(--blue)" stroke-width="1.8" stroke-linecap="round" stroke-linejoin="round"/></svg>
        Spülen und Entlüften von Solaranlagen
      </li>
      <li>
        <svg class="check-circle" viewBox="0 0 20 20"><path d="M17.2 6.2A8.3 8.3 0 1 0 18.3 10" fill="none" stroke="var(--blue)" stroke-width="1.8" stroke-linecap="round"/><path d="M6 9.5l3.4 3.4L18.5 3.5" fill="none" stroke="var(--blue)" stroke-width="1.8" stroke-linecap="round" stroke-linejoin="round"/></svg>
        Flexible, schnelle &amp; unkomplizierte Hilfe
      </li>
      <li>
        <svg class="check-circle" viewBox="0 0 20 20"><path d="M17.2 6.2A8.3 8.3 0 1 0 18.3 10" fill="none" stroke="var(--blue)" stroke-width="1.8" stroke-linecap="round"/><path d="M6 9.5l3.4 3.4L18.5 3.5" fill="none" stroke="var(--blue)" stroke-width="1.8" stroke-linecap="round" stroke-linejoin="round"/></svg>
        Austausch &amp; Modernisierung von Heizungsanlagen
      </li>
    </ul>

    <footer class="contact">
      <div class="contact__col contact__col--left">
        <div class="contact__lines">Standort – Lindach am Fluss<br>Lindenstraße 12<br>74812 Lindach am Fluss</div>
        <div class="contact__item"><svg viewBox="0 0 24 24"><path d="M6.6 2.5l3 3.3-1.8 2.6a13 13 0 0 0 7.8 7.8l2.6-1.8 3.3 3-2 3.1C11 20 4 13 3.5 4.5z" fill="#fff"/></svg>(0741) 40 52 18 9</div>
        <div class="contact__item"><svg viewBox="0 0 24 18"><rect x="1" y="1" width="22" height="16" fill="#fff"/><path d="M1 1l11 9 11-9" fill="none" stroke="var(--blue)" stroke-width="1.8"/></svg>info@brenntal-gmbh.de</div>
      </div>
      <div class="contact__divider"></div>
      <div class="contact__col contact__col--right">
        <div class="contact__lines">Standort – Eichenau im Walde<br>Birkenweg 4<br>72455 Eichenau im Walde</div>
        <div class="contact__item"><svg viewBox="0 0 24 24"><path d="M6.6 2.5l3 3.3-1.8 2.6a13 13 0 0 0 7.8 7.8l2.6-1.8 3.3 3-2 3.1C11 20 4 13 3.5 4.5z" fill="#fff"/></svg>(07422) 81 24 6</div>
        <div class="contact__item"><svg viewBox="0 0 24 24"><path d="M6.6 2.5l3 3.3-1.8 2.6a13 13 0 0 0 7.8 7.8l2.6-1.8 3.3 3-2 3.1C11 20 4 13 3.5 4.5z" fill="#fff"/></svg>(07455) 58 31 07</div>
        <div class="contact__item"><svg viewBox="0 0 24 18"><rect x="1" y="1" width="22" height="16" fill="#fff"/><path d="M1 1l11 9 11-9" fill="none" stroke="var(--blue)" stroke-width="1.8"/></svg>info@brenntal-gmbh.de</div>
      </div>
    </footer>
    <div class="web">www.brenntal-gmbh.de</div>
  </div>
</section>

<section class="flyer flyer--intro">
  <div class="flyer__inner">
    <svg class="hero" viewBox="0 0 488 424">
      <defs>
        <linearGradient id="heroRoom" x1="0" y1="0" x2="1" y2="0.6">
          <stop offset="0" stop-color="#d7d6d3"/>
          <stop offset="0.4" stop-color="#b5a796"/>
          <stop offset="0.7" stop-color="#e6e7e8"/>
          <stop offset="1" stop-color="#f2f3f4"/>
        </linearGradient>
      </defs>
      <polygon points="0,0 488,0 488,330 0,290" fill="url(#heroRoom)" role="img" aria-label="Foto: frierende Person im Strickpullover stellt ein Wandthermostat ein"/>
      <polygon points="0,290 488,330 488,352 0,312" fill="var(--blue)"/>
      <polygon points="0,318 488,358 488,364 0,324" fill="var(--yellow)"/>
      <polygon points="0,330 488,370 488,374 0,334" fill="var(--red)"/>
    </svg>
    <div class="brand">Brenntal GmbH</div>

    <h1 class="headline">Vorstellung:</h1>

    <ul class="facts">
      <li class="lead"><svg class="tick" viewBox="0 0 14 14"><path d="M1 7.5l4 4.5L13 1" fill="none" stroke="var(--red)" stroke-width="1.8" stroke-linecap="round" stroke-linejoin="round"/></svg>Familienunternehmen aus dem Kreis Lindach<br>Welches 2024 sein 18-jähriges Jubiläum feiert.</li>
      <li><svg class="tick" viewBox="0 0 14 14"><path d="M1 7.5l4 4.5L13 1" fill="none" stroke="var(--red)" stroke-width="1.8" stroke-linecap="round" stroke-linejoin="round"/></svg>geschultes Fachpersonal für alle „Leistungen“</li>
      <li><svg class="tick" viewBox="0 0 14 14"><path d="M1 7.5l4 4.5L13 1" fill="none" stroke="var(--red)" stroke-width="1.8" stroke-linecap="round" stroke-linejoin="round"/></svg>Gewissenhaftes und Zielorientiertes Arbeiten</li>
      <li><svg class="tick" viewBox="0 0 14 14"><path d="M1 7.5l4 4.5L13 1" fill="none" stroke="var(--red)" stroke-width="1.8" stroke-linecap="round" stroke-linejoin="round"/></svg>Eingetragener Meisterbetrieb Innung Lindach</li>
      <li><svg class="tick" viewBox="0 0 14 14"><path d="M1 7.5l4 4.5L13 1" fill="none" stroke="var(--red)" stroke-width="1.8" stroke-linecap="round" stroke-linejoin="round"/></svg>Ausbildungsbetrieb</li>
      <li><svg class="tick" viewBox="0 0 14 14"><path d="M1 7.5l4 4.5L13 1" fill="none" stroke="var(--red)" stroke-width="1.8" stroke-linecap="round" stroke-linejoin="round"/></svg>Langjährige Erfahrung mit Privathaushalten sowie<br>Hausverwaltungen</li>
    </ul>

    <div class="gallery">
      <div class="gallery__tile tile--bath" role="img" aria-label="Foto: modernes Badezimmer mit freistehender Badewanne"></div>
      <div class="gallery__tile tile--tech" role="img" aria-label="Foto: Handwerker mit Arbeitshandschuhen an einer Heiztherme"></div>
      <div class="gallery__tile tile--valves" role="img" aria-label="Foto: blaue Absperrventile und Rohrleitungen"></div>
    </div>

    <footer class="contact">
      <div class="contact__col contact__col--left">
        <div class="contact__lines">Standort – Lindach am Fluss<br>Lindenstraße 12<br>74812 Lindach am Fluss</div>
        <div class="contact__item"><svg viewBox="0 0 24 24"><path d="M6.6 2.5l3 3.3-1.8 2.6a13 13 0 0 0 7.8 7.8l2.6-1.8 3.3 3-2 3.1C11 20 4 13 3.5 4.5z" fill="#fff"/></svg>(0741) 40 52 18 9</div>
        <div class="contact__item"><svg viewBox="0 0 24 18"><rect x="1" y="1" width="22" height="16" fill="#fff"/><path d="M1 1l11 9 11-9" fill="none" stroke="var(--blue)" stroke-width="1.8"/></svg>info@brenntal-gmbh.de</div>
      </div>
      <div class="contact__divider"></div>
      <div class="contact__col contact__col--right">
        <div class="contact__lines">Standort – Eichenau im Walde<br>Birkenweg 4<br>72455 Eichenau im Walde</div>
        <div class="contact__item"><svg viewBox="0 0 24 24"><path d="M6.6 2.5l3 3.3-1.8 2.6a13 13 0 0 0 7.8 7.8l2.6-1.8 3.3 3-2 3.1C11 20 4 13 3.5 4.5z" fill="#fff"/></svg>(07422) 81 24 6</div>
        <div class="contact__item"><svg viewBox="0 0 24 24"><path d="M6.6 2.5l3 3.3-1.8 2.6a13 13 0 0 0 7.8 7.8l2.6-1.8 3.3 3-2 3.1C11 20 4 13 3.5 4.5z" fill="#fff"/></svg>(07455) 58 31 07</div>
        <div class="contact__item"><svg viewBox="0 0 24 18"><rect x="1" y="1" width="22" height="16" fill="#fff"/><path d="M1 1l11 9 11-9" fill="none" stroke="var(--blue)" stroke-width="1.8"/></svg>info@brenntal-gmbh.de</div>
      </div>
    </footer>
    <div class="web">www.brenntal-gmbh.de</div>
  </div>
</section>

</body>
</html>
```